Bramblewick Keystone

Looking for modern business cards.
Clean contemporary design.
Similar to this.
https://www.snapvorlo.net/imgview?src=https%3A%2F%2Fcdn.printquell.net%2Fprofessional_elegant_modern_black_plain_metal_business_card-a1b2c3d4e5f60718293a4b5c6d7e8f90_qwxyz_4tmpl_540.jpg&ref=https%3A%2F%2Fwww.printquell.net%2Fprofessional_elegant_modern_black_plain_metal_business_card-100200300400500600&id=7aB9cD3e-QR5TU&tid=Xyz_abc123defGH%3A&v=10abcDEFghiJKLmnoPQRstUVwxYZ0123456789abcd..x&w=540&h=540&bih=1360&biw=1061&q=modern%20business%20cards&ref2=0abcDEFghiJKLmnoPQRstUVwxYZ0123456789abcd&ia=mrc&ua=8

But I'd like the blue to look metallic.

```html
<!DOCTYPE html>
<html lang="en">
<head>
<meta charset="utf-8">
<title>Bramblewick Keystone – Business Card</title>
<link href="https://fonts.googleapis.com/css2?family=Questrial&display=swap" rel="stylesheet">
<style>
  :root {
    --backdrop: #3c4c58;
    --card-white: #ffffff;
    --ink-navy: #1d3a5c;
    --brand-teal: #1f8fb0;
    --metal-dark: #226f8c;
    --metal-mid: #3a93b2;
    --metal-light: #6cbcd6;
    --foil: #f4f9fb;
    --accent-red: #e0301e;
  }
  * { box-sizing: border-box; margin: 0; padding: 0; }
  html, body { width: 1200px; height: 900px; overflow: hidden; }
  body {
    background: var(--backdrop);
    font-family: "Questrial", "Century Gothic", sans-serif;
    display: flex;
    align-items: center;
    justify-content: center;
    gap: 40px;
  }
  .card {
    position: relative;
    width: 540px;
    height: 320px;
    border-radius: 26px;
    box-shadow: 0 14px 30px rgba(0,0,0,.35);
    overflow: hidden;
  }

  /* Front */
  .card--front { background: var(--card-white); }
  .brand-lockup {
    position: absolute;
    top: 88px;
    right: 42px;
    text-align: right;
  }
  .brand-lockup__row { display: flex; align-items: center; gap: 10px; justify-content: flex-end; }
  .brand-lockup__name {
    font-size: 31px;
    color: var(--brand-teal);
    letter-spacing: -0.5px;
    white-space: nowrap;
  }
  .brand-lockup__dot {
    width: 12px; height: 12px; border-radius: 50%;
    background: var(--accent-red);
  }
  .brand-lockup__tagline {
    margin-top: 4px;
    font-size: 10px;
    color: var(--brand-teal);
    white-space: nowrap;
  }
  .holder {
    position: absolute;
    left: 40px;
    top: 150px;
  }
  .holder__name { font-size: 26px; color: var(--ink-navy); }
  .holder__title { font-size: 15px; color: var(--brand-teal); margin-top: 2px; }
  .contact {
    position: absolute;
    left: 40px;
    right: 28px;
    bottom: 42px;
    display: flex;
    align-items: center;
    flex-wrap: nowrap;
    white-space: nowrap;
    gap: 8px;
    font-size: 12.5px;
    color: var(--ink-navy);
  }
  .contact__item { display: flex; align-items: center; gap: 5px; }
  .contact__icon { width: 13px; height: 13px; flex: none; }
  .contact__sep { color: var(--ink-navy); }

  /* Back – brushed metal */
  .card--back {
    background:
      repeating-linear-gradient(0deg, rgba(255,255,255,.06) 0 1px, rgba(0,0,0,.05) 1px 2px, transparent 2px 4px),
      repeating-linear-gradient(0deg, rgba(255,255,255,.04) 0 3px, rgba(0,0,0,.06) 3px 5px, transparent 5px 9px),
      linear-gradient(115deg, var(--metal-dark) 0%, var(--metal-mid) 30%, var(--metal-light) 48%, var(--metal-mid) 62%, var(--metal-dark) 100%);
    display: flex;
    flex-direction: column;
    align-items: center;
    justify-content: center;
  }
  .back-lockup__row { display: flex; align-items: center; gap: 12px; }
  .back-lockup__name {
    font-size: 38px;
    color: var(--foil);
    letter-spacing: -0.5px;
    white-space: nowrap;
  }
  .back-lockup__dot {
    width: 14px; height: 14px; border-radius: 50%;
    background: var(--foil);
  }
  .back-lockup__tagline {
    margin-top: 10px;
    font-size: 13px;
    letter-spacing: 1.5px;
    color: var(--foil);
    white-space: nowrap;
  }
</style>
</head>
<body>

  <section class="card card--front" aria-label="Business card front">
    <div class="brand-lockup">
      <div class="brand-lockup__row">
        <span class="brand-lockup__name">Bramblewick Keystone</span>
        <span class="brand-lockup__dot"></span>
      </div>
      <p class="brand-lockup__tagline">Steady Foundations for Growing Companies</p>
    </div>

    <div class="holder">
      <p class="holder__name">Your Name</p>
      <p class="holder__title">Job Title</p>
    </div>

    <div class="contact">
      <span class="contact__item">
        <svg class="contact__icon" viewBox="0 0 16 16" aria-hidden="true"><path fill="#1d3a5c" d="M2 5c0-2 2-3 6-3s6 1 6 3v1h-3V5H5v1H2zM4 7h8l2 6H2z"/></svg>
        000 000 0000
      </span>
      <span class="contact__sep">/</span>
      <span class="contact__item">
        <svg class="contact__icon" viewBox="0 0 16 16" aria-hidden="true"><rect x="1" y="3" width="14" height="10" fill="#1f8fb0"/><path d="M1 3l7 6 7-6" fill="none" stroke="#fff" stroke-width="1.2"/></svg>
        hi@bramblewick.com
      </span>
      <span class="contact__sep">/</span>
      <span class="contact__item">
        <svg class="contact__icon" viewBox="0 0 16 16" aria-hidden="true"><g fill="none" stroke="#1f8fb0" stroke-width="1.2"><circle cx="8" cy="8" r="6.5"/><ellipse cx="8" cy="8" rx="3" ry="6.5"/><path d="M1.5 8h13M2.5 4.8h11M2.5 11.2h11"/></g></svg>
        www.bramblewick.com
      </span>
    </div>
  </section>

  <section class="card card--back" aria-label="Business card back">
    <div class="back-lockup__row">
      <span class="back-lockup__name">Bramblewick Keystone</span>
      <span class="back-lockup__dot"></span>
    </div>
    <p class="back-lockup__tagline">“Steady Foundations for Growing Companies”</p>
  </section>

</body>
</html>
```